Velorix Flyer

PROJECT: Digital Flyer for VeloRix

Format
1920 × 1080 px (landscape, optimized for presentations and email)
Deliverables
• PDF
• PNG

About VeloRix
VeloRix is a Dutch B2B software company providing a unified CRM and customer journey platform. We help businesses manage the entire customer lifecycle — from first contact to loyal customer — by centralizing all touchpoints in one system.
What sets us apart:
Extreme ease of use. The system is self-guiding, shows only what's relevant per employee, and requires virtually no training. All channels (email, phone, chat, in-store) come together in one place with automatic task distribution. Built-in AI functions as a smart digital colleague that continuously learns.
Target audience:
Directors and sales managers at B2B companies with multiple customer contact channels.

Goal:
We want to create a flyer that sets us apart from other CRM platform providers. Our aim is to achieve this through simplicity and a professional appearance. The design should reflect our core value: ease of use. The recipient should feel compelled to engage with us — not overwhelmed by information, but intrigued by clarity. Less is more.

Required Text Elements
Headline:
"CRM that adapts to how you work"
Subline:
"Discover how VeloRix simplifies your sales process"
Call-to-action:
"See it in action — book a call"
Contact details:
• hello@velorix.nl
• 023-5718469
• velorix.com

Required Visual Elements
• VeloRix logo (attached)

Design Style
• Modern / Minimalist
• Professional / Business
• Tech / Futuristic
• Clean with plenty of whitespace

Tone of voice:
Clear, positive and customer-focused. Practical and accessible business style aimed at communicating concrete value for users.

Design inspiration — please review these websites:
• orbantal.com
• ravelo.app
• quendo.com
• tirameld.com
• gonwisp.com
What We DON'T Want
• Bold / In-your-face
• Dense / Compact
• Trendy / Experimental
• Childlike / Cheerful
• Playful / Cartoonish
• Busy / Chaotic
Colors
Use the color palette from velorix.com (blues, whites, clean professional tones).
[Exact hex codes used for element on the website:
#344054;
#1a1b1f;
#0254ac
#002249;
#e5edf7;
background-color: #fff; ]
Competitors (for context only — do NOT copy)
• brinvolt.nl
• kelmarin.com
• dortavecrm.com
• wexalunda.com
Budget
$150
Deadline
January 26, 2026

```html
<!DOCTYPE html>
<html lang="en">
<head>
<meta charset="utf-8">
<title>VeloRix Flyer</title>
<link rel="stylesheet" href="https://fonts.googleapis.com/css2?family=Open+Sans:wght@400;600;700&family=Raleway:wght@700&display=swap">
<style>
  :root {
    --stage: #595959;
    --white: #ffffff;
    --ink: #002249;
    --text: #344054;
    --brand: #0254ac;
    --band: #e5edf7;
    --navy-deep: #0c1a45;
    --navy-mid: #33489a;
    --mist: #ececee;
  }
  * { box-sizing: border-box; margin: 0; padding: 0; }
  html, body {
    width: 1200px; height: 737px; overflow: hidden;
    background: var(--stage);
  }
  .flyer {
    position: absolute; left: 78px; top: 79px;
    width: 1030px; height: 579px; overflow: hidden;
    background: var(--white);
    font-family: "Open Sans", Arial, sans-serif;
  }
  .backdrop {
    position: absolute; inset: 0 0 100px 0;
    background: linear-gradient(180deg, var(--mist) 0%, #f3f3f5 55%, var(--white) 100%);
  }
  .backdrop-chart { position: absolute; left: 0; top: 0; }
  .contact-band {
    position: absolute; left: 0; right: 0; bottom: 0; height: 100px;
    background: var(--band);
  }
  .hero-visual {
    position: absolute; left: 514px; top: 44px;
    width: 490px; height: 497px;
  }
  .hero-visual svg { display: block; }
  .brand {
    position: absolute; left: 57px; top: 44px;
    display: flex; align-items: center; gap: 12px;
  }
  .brand-dot {
    width: 36px; height: 36px; border-radius: 50%;
    background: var(--ink);
  }
  .brand-name {
    font-size: 40px; font-weight: 600; color: var(--ink);
    letter-spacing: -0.4px; line-height: 1;
  }
  .headline {
    position: absolute; left: 56px; top: 180px;
    font-size: 40px; font-weight: 700; line-height: 46px;
    color: var(--ink); letter-spacing: -0.2px;
  }
  .subline {
    position: absolute; left: 59px; top: 287px;
    font-size: 17px; color: var(--text);
  }
  .cta {
    position: absolute; left: 57px; top: 347px;
    width: 376px; height: 55px; border-radius: 28px;
    background: var(--brand); color: var(--white);
    display: flex; align-items: center; justify-content: center;
    font-family: "Raleway", Arial, sans-serif;
    font-size: 24px; font-weight: 700; letter-spacing: -0.3px;
  }
  .contacts {
    position: absolute; left: 62px; top: 504px;
    display: flex; align-items: center; gap: 28px;
    font-size: 17px; color: var(--text);
  }
  .contact-item { display: flex; align-items: center; gap: 7px; }
  .contact-item svg { display: block; }
</style>
</head>
<body>
  <main class="flyer">
    <div class="backdrop" role="img" aria-label="Faint light-grey photo of financial candlestick charts">
      <svg class="backdrop-chart" width="1030" height="479" viewBox="0 0 1030 479" aria-hidden="true">
        <g stroke="#ffffff" stroke-width="1.5" opacity="0.8">
          <line x1="32" y1="10" x2="32" y2="220"/><line x1="100" y1="120" x2="100" y2="290"/>
          <line x1="240" y1="90" x2="240" y2="260"/><line x1="290" y1="60" x2="290" y2="200"/>
          <line x1="348" y1="110" x2="348" y2="280"/><line x1="420" y1="90" x2="420" y2="230"/>
          <line x1="470" y1="150" x2="470" y2="330"/><line x1="560" y1="200" x2="560" y2="340"/>
        </g>
        <g fill="#ffffff" opacity="0.75">
          <rect x="24" y="20" width="16" height="100"/><rect x="92" y="140" width="16" height="60"/>
          <rect x="130" y="170" width="16" height="40"/><rect x="200" y="150" width="16" height="20"/>
          <rect x="232" y="100" width="16" height="70"/><rect x="282" y="80" width="16" height="80"/>
          <rect x="340" y="130" width="16" height="90"/><rect x="412" y="110" width="16" height="60"/>
          <rect x="462" y="170" width="16" height="80"/><rect x="552" y="220" width="16" height="60"/>
        </g>
      </svg>
    </div>
    <div class="contact-band"></div>

    <div class="hero-visual" role="img" aria-label="Dark blue duotone photo of a person using a smartphone with a network map and rising chart bars">
      <svg width="490" height="497" viewBox="0 0 490 497" aria-hidden="true">
        <defs>
          <radialGradient id="heroTone" cx="30%" cy="25%" r="85%">
            <stop offset="0" stop-color="#5a6db0"/>
            <stop offset="0.3" stop-color="var(--navy-mid)"/>
            <stop offset="0.65" stop-color="#1b2c68"/>
            <stop offset="1" stop-color="var(--navy-deep)"/>
          </radialGradient>
          <linearGradient id="heroShade" x1="0" y1="0" x2="1" y2="1">
            <stop offset="0" stop-color="#ffffff" stop-opacity="0.08"/>
            <stop offset="1" stop-color="#000000" stop-opacity="0.25"/>
          </linearGradient>
          <clipPath id="heroClip"><ellipse cx="245" cy="248.5" rx="245" ry="248.5"/></clipPath>
        </defs>
        <g clip-path="url(#heroClip)">
          <rect width="490" height="497" fill="url(#heroTone)"/>
          <rect width="490" height="497" fill="url(#heroShade)"/>
          <g stroke="#8fa0d6" stroke-width="1.2" opacity="0.55">
            <line x1="30" y1="330" x2="30" y2="440"/><line x1="70" y1="360" x2="70" y2="480"/>
            <line x1="120" y1="340" x2="120" y2="470"/><line x1="170" y1="380" x2="170" y2="497"/>
            <line x1="220" y1="350" x2="220" y2="497"/><line x1="270" y1="370" x2="270" y2="497"/>
            <line x1="320" y1="340" x2="320" y2="497"/><line x1="370" y1="360" x2="370" y2="480"/>
            <line x1="420" y1="330" x2="420" y2="460"/>
          </g>
          <g fill="#7f92cf" opacity="0.5">
            <rect x="24" y="350" width="12" height="40"/><rect x="64" y="390" width="12" height="50"/>
            <rect x="114" y="370" width="12" height="60"/><rect x="164" y="410" width="12" height="50"/>
            <rect x="214" y="380" width="12" height="70"/><rect x="264" y="400" width="12" height="60"/>
            <rect x="314" y="360" width="12" height="80"/><rect x="364" y="385" width="12" height="55"/>
            <rect x="414" y="350" width="12" height="60"/>
          </g>
          <g stroke="#9fb0e0" stroke-width="1" fill="none" opacity="0.35">
            <path d="M60 140 L120 90 L180 120 L150 180 L90 200 Z"/>
            <path d="M120 90 L150 180 M60 140 L180 120"/>
          </g>
        </g>
      </svg>
    </div>

    <div class="brand">
      <span class="brand-dot"></span>
      <span class="brand-name">VeloRix</span>
    </div>

    <h1 class="headline">CRM that adapts<br>to how you work</h1>
    <p class="subline">Discover how VeloRix simplifies your sales process</p>
    <a class="cta">See it in action – book a call</a>

    <div class="contacts">
      <span class="contact-item">
        <svg width="18" height="13" viewBox="0 0 18 13"><path d="M0 0h18L9 6.5z" fill="var(--ink)"/><path d="M0 1.8 9 8.3l9-6.5V13H0z" fill="var(--ink)"/></svg>
        hello@velorix.nl
      </span>
      <span class="contact-item">
        <svg width="15" height="15" viewBox="0 0 24 24"><path fill="var(--ink)" d="M6.6 10.8a15.1 15.1 0 0 0 6.6 6.6l2.2-2.2c.3-.3.7-.4 1-.2 1.1.4 2.3.6 3.6.6.6 0 1 .4 1 1V20c0 .6-.4 1-1 1A17 17 0 0 1 3 4c0-.6.4-1 1-1h3.5c.6 0 1 .4 1 1 0 1.3.2 2.5.6 3.6.1.3 0 .7-.2 1z"/></svg>
        023-5718469
      </span>
      <span class="contact-item">
        <svg width="17" height="17" viewBox="0 0 24 24" fill="none" stroke="var(--ink)" stroke-width="1.8"><circle cx="12" cy="12" r="10"/><path d="M2 12h20M12 2c3 3 3 17 0 20M12 2c-3 3-3 17 0 20"/></svg>
        velorix.com
      </span>
    </div>
  </main>
</body>
</html>
```